Crash Reapirer business card design

We are a crash repair business based in a small country town in South Australia with our own spray booth. We do all types of repairs for both insurance companies and private jobs. We also replace broken windscreens.
We usually have the KVL logo on our cards because we are KVL approved repairers.
We would also like the JPO (Vehicle Guild Federation)logo because we are a member for them also.
If the card could incorporate black, grey, white and silver colours that would be excellent.
We do not have our own logo if 1 could be created that would be great.

Industry/Entity Type

Insurance

Contact Information for Business Card

Dorvick Crash Repairs
47 Tulloch Ave, Renmark SA 5341
Ph 08 85213077 Fax 08 85213358
Kent 0412658341
Email - dorcrash@fernmail.com

We do private & insurance work, windscreen replacements on all makes & models of cars

```html
<!DOCTYPE html>
<html lang="en">
<head>
<meta charset="utf-8">
<title>Dorvick Crash Repairs – Business Card</title>
<link rel="stylesheet" href="https://fonts.googleapis.com/css2?family=Fjalla+One&family=Open+Sans:wght@400;700&display=swap">
<style>
  :root {
    --card-bg: #2e2e2e;
    --card-edge: #3a3a3a;
    --white: #ffffff;
    --silver: #e6e6e6;
    --grey: #8c8c8c;
    --badge-blue: #3b55a0;
  }
  html, body {
    margin: 0;
    padding: 0;
    width: 1200px;
    height: 740px;
    overflow: hidden;
    background: var(--card-bg);
  }
  .card {
    position: relative;
    width: 1200px;
    height: 740px;
    box-sizing: border-box;
    border: 1px solid var(--card-edge);
    background: var(--card-bg);
    font-family: "Open Sans", Arial, sans-serif;
    color: var(--white);
  }
  .brand-mark {
    position: absolute;
    left: 138px;
    top: 144px;
    width: 143px;
    height: 145px;
    background: var(--white);
  }
  .brand-name {
    position: absolute;
    left: 318px;
    top: 128px;
    margin: 0;
    font-family: "Fjalla One", "Arial Narrow", sans-serif;
    font-weight: 400;
    font-size: 88px;
    line-height: 88px;
    color: var(--silver);
    letter-spacing: 0.5px;
  }
  .brand-name span { display: block; }
  .services {
    position: absolute;
    left: 115px;
    top: 391px;
    margin: 0;
    padding: 0;
    list-style: none;
    font-size: 29px;
    line-height: 44px;
    color: var(--grey);
  }
  .services .dot { margin-right: 6px; }
  .services .gap { margin-left: 16px; }
  .contact {
    position: absolute;
    left: 114px;
    top: 533px;
    font-size: 27px;
    line-height: 42px;
    color: var(--white);
  }
  .contact p { margin: 0; }
  .contact .address { padding-left: 20px; }
  .contact b { font-weight: 700; }
  .contact .dot { font-size: 20px; vertical-align: 3px; margin-right: 4px; }
  .badges {
    position: absolute;
    left: 878px;
    top: 538px;
    display: flex;
    gap: 6px;
  }
  .badge {
    width: 97px;
    height: 113px;
  }
  .badge--approved { background: var(--white); }
  .badge--member {
    width: 113px;
    box-sizing: border-box;
    background: var(--badge-blue);
    border: 4px solid var(--white);
  }
</style>
</head>
<body>
  <main class="card">
    <div class="brand-mark" aria-hidden="true"></div>
    <h1 class="brand-name"><span>Dorvick</span><span>Crash Repairs</span></h1>

    <ul class="services">
      <li><span class="dot">•</span>Private &amp; Insurance work <span class="gap">•</span> Windscreen Replacements</li>
      <li><span class="dot">•</span>All makes &amp; models of cars</li>
    </ul>

    <div class="contact">
      <p class="address">47 Tulloch Ave, Renmark SA 5341</p>
      <p><span class="dot">•</span><b>Ph:</b> 08 85213077 <span class="dot">•</span><b>Fax:</b> 08 85213358</p>
      <p><span class="dot">•</span><b>Kent:</b> 0412658341<span class="dot">•</span> <b>Email</b>-dorcrash@fernmail.com</p>
    </div>

    <div class="badges">
      <div class="badge badge--approved" role="img" aria-label="KVL approved repairer badge"></div>
      <div class="badge badge--member" role="img" aria-label="JPO Vehicle Guild Federation member badge"></div>
    </div>
  </main>
</body>
</html>
```